Business Card Design

Need a card designed to fit the tax preparation and accounting profession. Would like to include the following on side two of the card:

Tax Preparation and Audit Representation for:
Individuals
Partnerships
Corporations
Estates
Trusts
Other entities with tax reporting requirements

Industry/Entity Type

Accounting

Contact Information for Business Card

Marlowe & Associates
Tax and Business Services
Derek P Halvorsen II, EA, MS
Enrolled Agent P07385169
4172 Sorrel Avenue, Suite B
Citrus Heights, CA 95847
(916) 284-6051
Email: ledgerpro782@mailbrook.net
www.ledgerhelpcenter.net

```html
<!DOCTYPE html>
<html lang="en">
<head>
<meta charset="utf-8">
<title>Marlowe &amp; Associates – Business Card</title>
<link href="https://fonts.googleapis.com/css2?family=Marcellus+SC&family=PT+Sans:wght@400;700&display=swap" rel="stylesheet">
<style>
  :root {
    --crimson: #c8203f;
    --crimson-deep: #a3122d;
    --crimson-light: #dc4865;
    --ink: #2b2b2b;
    --grey: #6a6a6a;
    --paper: #ffffff;
    --backdrop: #e9e7e4;
  }
  * { box-sizing: border-box; margin: 0; padding: 0; }
  html, body { width: 1200px; height: 800px; overflow: hidden; }
  body {
    background: var(--backdrop);
    font-family: "PT Sans", sans-serif;
    display: flex;
    align-items: center;
    justify-content: center;
    gap: 40px;
  }
  .card {
    position: relative;
    width: 540px;
    height: 310px;
    overflow: hidden;
    box-shadow: 0 6px 18px rgba(0,0,0,.18);
  }

  /* Back side */
  .card-back {
    background: linear-gradient(160deg, var(--crimson-light) 0%, var(--crimson) 50%, var(--crimson-deep) 100%);
    color: var(--paper);
    text-align: center;
  }
  .card-back .facet {
    position: absolute; inset: 0;
    background: linear-gradient(115deg, transparent 45%, rgba(255,255,255,.08) 45%, rgba(255,255,255,.08) 70%, transparent 70%);
  }
  .back-content { position: relative; padding-top: 38px; }
  .back-firm {
    font-family: "Marcellus SC", serif;
    font-size: 27px;
    font-weight: 400;
    letter-spacing: 1px;
  }
  .back-tagline {
    font-family: "Marcellus SC", serif;
    font-size: 17px;
    margin-top: 4px;
  }
  .back-mark {
    width: 62px; height: 62px;
    border: 2px solid var(--paper);
    border-radius: 50%;
    margin: 22px auto 20px;
  }
  .services { font-size: 13px; line-height: 1.55; }

  /* Front side */
  .card-front { background: var(--paper); color: var(--ink); }
  .brand {
    position: absolute; top: 22px; left: 0; right: 0; height: 70px;
  }
  .brand-rule {
    position: absolute; left: 0; top: 24px; width: 38px; height: 2px; background: var(--crimson);
  }
  .brand-circle {
    position: absolute; left: 38px; top: 0;
    width: 50px; height: 50px; border-radius: 50%;
    border: 2px solid var(--crimson);
  }
  .brand-name {
    position: absolute; left: 102px; top: 6px;
    font-family: "Marcellus SC", serif; font-size: 24px; letter-spacing: .5px; color: var(--ink);
  }
  .brand-tagline {
    position: absolute; left: 102px; top: 36px;
    font-family: "Marcellus SC", serif; font-size: 18px; color: var(--ink);
  }
  .brand-underline {
    position: absolute; left: 102px; right: 22px; top: 62px; height: 2px; background: var(--crimson);
  }
  .person { position: absolute; left: 28px; top: 106px; }
  .person-name {
    font-family: "Marcellus SC", serif; font-size: 20px; font-weight: 400; color: var(--crimson); letter-spacing: .5px;
  }
  .person-title { font-size: 11px; color: var(--grey); letter-spacing: 1px; margin-top: 2px; }
  .contacts { list-style: none; margin-top: 8px; font-size: 12.5px; color: var(--ink); }
  .contacts li { display: flex; align-items: center; gap: 7px; height: 18px; }
  .contacts svg { width: 12px; height: 12px; flex: none; }
  .address-band {
    position: absolute; left: 0; right: 160px; bottom: 0; height: 30px;
    background: var(--crimson);
    color: var(--paper);
    font-size: 10.5px; letter-spacing: .3px; text-transform: uppercase;
    white-space: nowrap;
    display: flex; align-items: center; padding-left: 14px;
  }
  .portrait {
    position: absolute; right: 10px; bottom: 0;
    width: 150px; height: 170px;
    background: linear-gradient(180deg, #b88a6c 0%, #7a5a45 45%, #9fc27a 65%, #2a2a2a 100%);
    border-radius: 60px 60px 0 0;
  }
</style>
</head>
<body>

  <section class="card card-back" aria-label="Card back">
    <div class="facet"></div>
    <div class="back-content">
      <h1 class="back-firm">Marlowe &amp; Associates</h1>
      <p class="back-tagline">Tax &amp; Business Services</p>
      <div class="back-mark"></div>
      <p class="services">
        Tax Preparation and Audit Representation for:<br>
        Individuals | Partnerships | Corporations | Estates | Trusts<br>
        Other entities with tax reporting requirements
      </p>
    </div>
  </section>

  <section class="card card-front" aria-label="Card front">
    <div class="brand">
      <span class="brand-rule"></span>
      <span class="brand-circle"></span>
      <span class="brand-name">Marlowe &amp; Associates</span>
      <span class="brand-tagline">Tax &amp; Business Services</span>
      <span class="brand-underline"></span>
    </div>

    <div class="person">
      <h2 class="person-name">Derek P Halvorsen II, MS</h2>
      <p class="person-title">ENROLLED AGENT</p>
      <ul class="contacts">
        <li>
          <svg viewBox="0 0 12 12"><circle cx="6" cy="6" r="6" fill="#c8203f"/><path d="M4 3.2h1.2l.5 1.5-.7.6a4 4 0 0 0 1.7 1.7l.6-.7 1.5.5V8a.8.8 0 0 1-.8.8A4.8 4.8 0 0 1 3.2 4 .8.8 0 0 1 4 3.2z" fill="#fff"/></svg>
          (916) 284-6051
        </li>
        <li>
          <svg viewBox="0 0 12 12"><circle cx="6" cy="6" r="6" fill="#c8203f"/><rect x="3" y="4" width="6" height="4.2" fill="none" stroke="#fff" stroke-width=".9"/><path d="M3 4l3 2.3L9 4" fill="none" stroke="#fff" stroke-width=".9"/></svg>
          ledgerpro782@mailbrook.net
        </li>
        <li>
          <svg viewBox="0 0 12 12"><circle cx="6" cy="6" r="6" fill="#c8203f"/><circle cx="6" cy="6" r="3.2" fill="none" stroke="#fff" stroke-width=".8"/><path d="M2.8 6h6.4M6 2.8c-1.6 1.8-1.6 4.6 0 6.4M6 2.8c1.6 1.8 1.6 4.6 0 6.4" fill="none" stroke="#fff" stroke-width=".7"/></svg>
          www.ledgerhelpcenter.net
        </li>
        <li class="license">P07385169</li>
      </ul>
    </div>

    <div class="address-band">4172 Sorrel Avenue, Suite B, Citrus Heights, CA 95847</div>
    <div class="portrait" role="img" aria-label="Portrait photo of the enrolled agent in a dark suit and green shirt"></div>
  </section>

</body>
</html>
```